Set of 6 Icons and buttons required

We have written a windows based app which gives clients access to reports etc.

We are a multichannel epos company

We require 6 buttons and icons along with a suggested font to use and a background for the form.

I have attatched a mock up of what we require from the chosen designer.

The buttons are as follows :

Stockcard ( This is a program which customers can enter stock and check stock levels etc )

Reports ( as the title says )

Stock ( This for making adjustments )

Goods ( this is for booking goods in )

Settings ( As title says )

Help ( As title says )

Dimensions
---------------

The form : 296x268
Buttons : 218x36
Icons on button : 32x32
Text size : Size 10

If you look at the attatched document this is something I put together just to show what we are looking once we put all the components together

Our website is q-ledgora.co.uk

Target Market(s)

B2B

Industry/Entity Type

It Company

```html
<!DOCTYPE html>
<html lang="en">
<head>
<meta charset="utf-8">
<title>q-ledgora launcher</title>
<link rel="stylesheet" href="https://fonts.googleapis.com/css2?family=Open+Sans:wght@300;700&display=swap">
<style>
  :root {
    --bg-top: #0f2a62;
    --bg-bottom: #4b75c6;
    --panel: #2b3371;
    --btn-top: #4350ad;
    --btn-bottom: #2a3283;
    --btn-text: #ffffff;
    --active-top: #ffffff;
    --active-bottom: #c9c9c9;
    --active-text: #555555;
    --icon-line: #e4e6f5;
    --icon-active: #5a5a5a;
    --brand: #e8ebf7;
    --brand-square: #2c7fd0;
  }
  html, body {
    margin: 0;
    padding: 0;
    width: 1200px;
    height: 1117px;
    overflow: hidden;
  }
  body {
    background: linear-gradient(to bottom, var(--bg-top) 0%, var(--bg-bottom) 100%);
    font-family: "Open Sans", Verdana, sans-serif;
    position: relative;
  }
  .launcher {
    position: absolute;
    left: 339px;
    top: 324px;
    width: 522px;
    height: 470px;
    background: var(--panel);
    box-shadow: 0 0 2px rgba(0,0,0,0.35);
  }
  .close-button {
    position: absolute;
    left: 489px;
    top: 10px;
    width: 24px;
    height: 24px;
  }
  .brand-name {
    position: absolute;
    left: 58px;
    top: 265px;
    transform: translate(-50%, -50%) rotate(-90deg);
    font-weight: 300;
    font-size: 44px;
    letter-spacing: 1px;
    color: var(--brand);
    white-space: nowrap;
  }
  .brand-square {
    position: absolute;
    left: 20px;
    top: 375px;
    width: 76px;
    height: 76px;
    background: var(--brand-square);
  }
  .menu {
    position: absolute;
    left: 120px;
    top: 45px;
    margin: 0;
    padding: 0;
    list-style: none;
  }
  .menu-button {
    display: flex;
    align-items: center;
    width: 395px;
    height: 65px;
    margin-bottom: 4px;
    background: linear-gradient(to bottom, var(--btn-top), var(--btn-bottom));
    color: var(--btn-text);
    font-weight: 700;
    font-size: 23px;
    letter-spacing: 0.5px;
  }
  .menu-button.is-active {
    background: linear-gradient(to bottom, var(--active-top), var(--active-bottom));
    color: var(--active-text);
  }
  .menu-icon {
    width: 56px;
    height: 56px;
    margin: 0 10px 0 5px;
    flex: none;
    stroke: var(--icon-line);
    fill: none;
    stroke-width: 3;
  }
  .is-active .menu-icon { stroke: var(--icon-active); }
  .menu-icon .solid { fill: var(--icon-line); stroke: none; }
  .is-active .menu-icon .solid { fill: var(--icon-active); }
</style>
</head>
<body>
  <div class="launcher">
    <svg class="close-button" viewBox="0 0 24 24" aria-label="Close">
      <path d="M5 5 L19 19 M19 5 L5 19" stroke="#d9dbe6" stroke-width="5" stroke-linecap="round"/>
    </svg>
    <div class="brand-name">q-ledgora</div>
    <div class="brand-square"></div>

    <ul class="menu">
      <li class="menu-button">
        <svg class="menu-icon" viewBox="0 0 56 56"><circle cx="28" cy="28" r="25"/>
          <rect x="14" y="16" width="28" height="24"/>
          <path d="M14 21 H42 M18 26 H38 M18 30 H38 M18 34 H38" stroke-width="2"/></svg>
        Stockcard
      </li>
      <li class="menu-button is-active">
        <svg class="menu-icon" viewBox="0 0 56 56"><circle cx="28" cy="28" r="25"/>
          <path class="solid" d="M26 14 A14 14 0 1 0 40 30 L26 30 Z"/>
          <path class="solid" d="M30 12 A14 14 0 0 1 43 25 L30 25 Z"/></svg>
        Reports
      </li>
      <li class="menu-button">
        <svg class="menu-icon" viewBox="0 0 56 56"><circle cx="28" cy="28" r="25"/>
          <path d="M13 32 L19 25 L25 31 L31 24 L37 30 L43 24" stroke-linejoin="round"/></svg>
        Stock
      </li>
      <li class="menu-button">
        <svg class="menu-icon" viewBox="0 0 56 56"><circle cx="28" cy="28" r="25"/>
          <rect class="solid" x="15" y="29" width="12" height="12"/>
          <rect class="solid" x="29" y="29" width="12" height="12"/>
          <rect class="solid" x="22" y="16" width="12" height="11"/></svg>
        Goods
      </li>
      <li class="menu-button">
        <svg class="menu-icon" viewBox="0 0 56 56"><circle cx="28" cy="28" r="25"/>
          <circle cx="28" cy="28" r="9" stroke-width="5"/>
          <path d="M28 11 V17 M28 39 V45 M11 28 H17 M39 28 H45 M16 16 L20 20 M36 36 L40 40 M40 16 L36 20 M20 36 L16 40" stroke-width="5"/></svg>
        Settings
      </li>
      <li class="menu-button">
        <svg class="menu-icon" viewBox="0 0 56 56"><circle cx="28" cy="28" r="25"/>
          <path d="M20 22 A8 8 0 1 1 31 29 Q28 31 28 35 V36" stroke-width="5" stroke-linecap="round"/>
          <circle class="solid" cx="28" cy="43" r="3"/></svg>
        Help
      </li>
    </ul>
  </div>
</body>
</html>
```